Wholesale company needs a sales brochure for our latest gadget- Orbo Tag. We sell to retailers

We need a sale brochure for our new product- Orbo/Velt Tag. It's an elegant little device that connects to any smartphone using an APP and let you locate your keys or your phone when you can't find them. We would like to see a design that uses the colors: Light blue, Black and metallic silver. The final design should communicate tech and innovative product. We need a total of 4 pages of 8.5x11'' (US letter size) to describe:
- Product benefits
- Product in use
- Display solution
- Profit generator
- Success story

Attached below are photos of the packaging and the display for your reference. Better photos will be sent later.
Please keep in mind that this product should be displayed on the counter with high foot traffic OR hang on hooks on a display fixture in the store.

This brochure will be used mainly to be sent digitally via email BUT we will also print it and will be mailing copies to our buyers.

Target Market(s)

Retailers and Distributors.
Small to mid-size retail stores:
- Electronic stores
- Convenient store
- Cellphone stores
- Gift stores

Industry/Entity Type

Retail

Font styles to use
Sans Serif

Colors
0692cd
ffffff
f3f1f8
33a6d7
85cae6

Requirements
Must have
• Must have:
• - "techie" and innovative look to go hand in hand with the product itself.
• - "in use" photos
• - "Description of the product"
• - Spec info
Nice to have
• Pattern or abstract design on background behind the text and images

```html
<!DOCTYPE html>
<html lang="en">
<head>
<meta charset="utf-8">
<title>Orbo Tag Sales Brochure</title>
<link href="https://fonts.googleapis.com/css2?family=Exo+2:wght@600;700;800&family=Lato:wght@400;700&display=swap" rel="stylesheet">
<style>
:root{
  --blue:#0692cd;
  --blue-deep:#0b4fc4;
  --blue-dark:#0a3fae;
  --sky:#33a6d7;
  --sky-light:#85cae6;
  --white:#ffffff;
  --mist:#f3f1f8;
  --silver:#d6d8dc;
  --ink:#111111;
  --stage:#a9aaac;
}
*{box-sizing:border-box;margin:0;padding:0}
html,body{width:989px;height:1200px;overflow:hidden;background:var(--stage)}
body{position:relative;font-family:"Lato",sans-serif;color:var(--ink)}
.page{position:absolute;overflow:hidden}
.page--cover{left:128px;top:96px;width:362px;height:464px;background:linear-gradient(135deg,var(--white),var(--mist) 60%,#e2e2e6)}
.page--back{left:518px;top:96px;width:362px;height:464px;background:linear-gradient(160deg,var(--blue-deep),#1565d8 50%,var(--blue-dark))}
.page--two{left:133px;top:596px;width:369px;height:504px;background:linear-gradient(135deg,var(--white),var(--mist))}
.page--three{left:502px;top:596px;width:376px;height:504px;background:linear-gradient(160deg,var(--blue-deep),#1565d8 55%,var(--blue-dark))}
.deco{position:absolute;inset:0;width:100%;height:100%}
.abs{position:absolute}
.brand{font-family:"Lato",sans-serif;font-weight:700;letter-spacing:-0.5px;line-height:1}
.photo{position:absolute;border-radius:4px}
.headline{font-family:"Exo 2",sans-serif;font-weight:800;line-height:1.1}
.small{font-size:7.5px;line-height:1.35}
.boxed-title{position:absolute;border:1.5px solid var(--white);color:var(--white);text-align:center;font-family:"Lato",sans-serif}
.pins{position:absolute;display:flex;justify-content:space-between}
.pin{display:flex;flex-direction:column;align-items:center;width:64px}
.pin svg{width:46px;height:60px}
.pin span{font-size:7.5px;font-weight:700;text-align:center;line-height:1.2;margin-top:8px;text-transform:uppercase}
.url{font-size:9px;letter-spacing:2px}
.dots{position:absolute;display:flex;gap:4px;justify-content:center;left:0;width:100%}
.dots i{display:block;border-radius:50%;background:var(--white)}
.contact{position:absolute;left:0;width:100%;text-align:center;color:var(--white);font-size:7.5px;line-height:10px}
.use-list{position:absolute;left:20px;top:88px;width:340px;list-style:none;color:var(--white)}
.use-list li{display:flex;gap:12px;align-items:flex-start;margin-bottom:9px;font-size:7.5px;line-height:1.35}
.use-list svg{flex:none;width:16px;height:16px}
</style>
</head>
<body>

<!-- Cover -->
<section class="page page--cover">
  <svg class="deco" viewBox="0 0 362 464" preserveAspectRatio="none" aria-hidden="true">
    <path d="M0 0 H110 C30 90 10 250 80 370 C110 420 150 450 200 464 H0 Z" fill="var(--blue)"/>
    <path d="M0 0 H70 C10 100 0 260 60 380 C85 425 120 450 150 464 H0 Z" fill="var(--blue-deep)"/>
    <path d="M110 0 C30 90 10 250 80 370 C110 420 150 450 200 464" fill="none" stroke="var(--sky-light)" stroke-width="3"/>
  </svg>
  <div class="abs brand" style="right:30px;top:26px;font-size:38px;color:var(--ink)">Orbo Tag</div>
  <div class="photo" role="img" aria-label="Four triangular tracker tags in black, light blue, pink and silver fanned out" style="left:48px;top:84px;width:276px;height:224px;background:linear-gradient(135deg,#2a2a2a 0%,var(--sky) 35%,#c8246e 60%,var(--silver) 85%);opacity:.9"></div>
  <div class="abs headline" style="right:29px;top:318px;font-size:25px;text-align:right">FIND YOUR PHONE<br><span style="color:var(--blue)">FIND YOUR KEYS</span></div>
  <p class="abs small" style="right:29px;top:388px;width:250px;text-align:right">Track the things that matter to you most with our Bluetooth Finder. Just attach it to your keys, pair it with our intuitive app and viola! Lost is now FOUND.</p>
  <div class="abs url" style="right:29px;top:434px">www.orbotag-demo.com</div>
</section>

<!-- Back -->
<section class="page page--back">
  <svg class="deco" viewBox="0 0 362 464" preserveAspectRatio="none" aria-hidden="true">
    <path d="M160 0 C240 40 300 20 362 60 V0 Z" fill="var(--blue)" opacity=".5"/>
    <path d="M0 300 C90 250 200 330 362 270 V464 H0 Z" fill="var(--blue)" opacity=".35"/>
    <path d="M345 70 C380 180 380 300 345 420" fill="none" stroke="var(--white)" stroke-width="5" opacity=".9"/>
  </svg>
  <div class="boxed-title" style="left:114px;top:68px;width:140px;height:28px;padding-top:7px;font-size:12px">OF THE PRODUCT</div>
  <div class="abs" style="left:134px;top:60px;width:100px;background:#1660d6;color:var(--white);text-align:center;font-size:12px;line-height:14px">Description</div>
  <p class="abs small" style="left:86px;top:110px;width:192px;text-align:center;color:var(--white);font-size:7px">The ultimate tracking device - designed with you, the consumer in mind. Pick from our collection of sleek colors carefully, and know that each one will give you the superpower to find!</p>
  <div class="abs brand" style="left:0;width:100%;top:176px;text-align:center;font-size:34px;color:var(--white)">Orbo Tag</div>
  <div class="dots" style="top:222px" aria-hidden="true"><i style="width:10px;height:10px"></i><i style="width:10px;height:10px"></i><i style="width:10px;height:10px"></i><i style="width:10px;height:10px"></i></div>
  <div class="contact" style="top:240px">
    <strong>OUR OFFICE</strong><br>48 Harbor Lane, Suite 210<br>Fairview, NC 20000<br>(555) 014-2290
  </div>
  <div class="contact" style="top:283px">hello@orbotag-demo.com<br>www.orbotag-demo.com</div>
  <div class="dots" style="top:318px;gap:5px" aria-hidden="true"><i style="width:7px;height:7px"></i><i style="width:7px;height:7px"></i><i style="width:7px;height:7px"></i><i style="width:7px;height:7px"></i></div>
  <div class="pins" style="left:30px;width:306px;top:356px;color:var(--white)">
    <div class="pin"><svg viewBox="0 0 44 56"><path d="M22 55 C10 40 2 30 2 20 A20 20 0 0 1 42 20 C42 30 34 40 22 55Z" fill="var(--blue)" stroke="#fff" stroke-width="1.5"/><rect x="13" y="14" width="18" height="11" rx="2" fill="#fff"/><rect x="20" y="25" width="4" height="9" fill="#fff"/></svg><span>Selfie camera<br>remote</span></div>
    <div class="pin"><svg viewBox="0 0 44 56"><path d="M22 55 C10 40 2 30 2 20 A20 20 0 0 1 42 20 C42 30 34 40 22 55Z" fill="var(--blue)" stroke="#fff" stroke-width="1.5"/><rect x="16" y="9" width="12" height="21" rx="2" fill="none" stroke="#fff" stroke-width="2"/></svg><span>Find your<br>phone</span></div>
    <div class="pin"><svg viewBox="0 0 44 56"><path d="M22 55 C10 40 2 30 2 20 A20 20 0 0 1 42 20 C42 30 34 40 22 55Z" fill="var(--blue)" stroke="#fff" stroke-width="1.5"/><rect x="11" y="14" width="22" height="15" rx="2" fill="#fff"/><rect x="18" y="10" width="8" height="5" rx="1" fill="none" stroke="#fff" stroke-width="2"/></svg><span>Find your<br>bag</span></div>
    <div class="pin"><svg viewBox="0 0 44 56"><path d="M22 55 C10 40 2 30 2 20 A20 20 0 0 1 42 20 C42 30 34 40 22 55Z" fill="var(--blue)" stroke="#fff" stroke-width="1.5"/><circle cx="27" cy="14" r="5" fill="none" stroke="#fff" stroke-width="2.5"/><path d="M24 18 L14 29 M17 26 L20 29" stroke="#fff" stroke-width="2.5"/></svg><span>Find your<br>keys</span></div>
  </div>
</section>

<!-- Page 2 -->
<section class="page page--two">
  <svg class="deco" viewBox="0 0 369 504" preserveAspectRatio="none" aria-hidden="true">
    <path d="M170 0 H369 V470 C355 420 340 340 322 270 C300 190 250 90 170 0 Z" fill="var(--blue-deep)"/>
    <path d="M130 0 C190 50 240 110 262 170" fill="none" stroke="var(--blue)" stroke-width="10" opacity=".8"/>
  </svg>
  <div class="abs brand" style="left:24px;top:38px;font-size:34px">Orbo Tag</div>
  <div class="photo" role="img" aria-label="Three triangular tags in light blue, pink and black stacked vertically" style="left:23px;top:88px;width:60px;height:164px;background:linear-gradient(180deg,var(--sky),#c8246e 50%,#222)"></div>
  <div class="abs" style="left:97px;top:152px;font-size:26px;font-weight:700">+</div>
  <div class="photo" role="img" aria-label="Silver triangular tag" style="left:114px;top:124px;width:72px;height:58px;background:linear-gradient(135deg,#eceef0,var(--silver))"></div>
  <div class="abs headline" style="left:110px;top:196px;font-size:24px">1 FREE</div>
  <div class="photo" role="img" aria-label="Retail blister package with light blue tag attached to a set of keys" style="left:223px;top:24px;width:120px;height:252px;background:linear-gradient(180deg,#3a3a3a 0 16%,#e6e8eb 16%,#cfd3d8)"></div>
  <h2 class="abs" style="left:22px;top:280px;font-size:13px;color:var(--blue-deep);font-weight:700">Product benefits</h2>
  <p class="abs small" style="left:22px;top:302px;width:292px">We had a problem... where is my phone? We weren't the only ones. Our friends and family all seemed to loose their phone, keys, purse or remote on a regular basis. So we decided to solve the problem once and for all. After years of working with customers all around the globe, we have refined and perfected something that is more than just a key finder. It's a phone finder, location tracker, camera remote. It's the future.</p>
  <div class="pins" style="left:30px;width:300px;top:384px">
    <div class="pin"><svg viewBox="0 0 44 56"><path d="M22 55 C10 40 2 30 2 20 A20 20 0 0 1 42 20 C42 30 34 40 22 55Z" fill="var(--blue-deep)"/><rect x="13" y="14" width="18" height="11" rx="2" fill="#fff"/><rect x="20" y="25" width="4" height="9" fill="#fff"/></svg><span>Selfie camera<br>remote</span></div>
    <div class="pin"><svg viewBox="0 0 44 56"><path d="M22 55 C10 40 2 30 2 20 A20 20 0 0 1 42 20 C42 30 34 40 22 55Z" fill="var(--blue-deep)"/><rect x="16" y="9" width="12" height="21" rx="2" fill="none" stroke="#fff" stroke-width="2"/></svg><span>Find your<br>phone</span></div>
    <div class="pin"><svg viewBox="0 0 44 56"><path d="M22 55 C10 40 2 30 2 20 A20 20 0 0 1 42 20 C42 30 34 40 22 55Z" fill="var(--blue-deep)"/><rect x="11" y="14" width="22" height="15" rx="2" fill="#fff"/><rect x="18" y="10" width="8" height="5" rx="1" fill="none" stroke="#fff" stroke-width="2"/></svg><span>Find your<br>bag</span></div>
    <div class="pin"><svg viewBox="0 0 44 56"><path d="M22 55 C10 40 2 30 2 20 A20 20 0 0 1 42 20 C42 30 34 40 22 55Z" fill="var(--blue-deep)"/><circle cx="27" cy="14" r="5" fill="none" stroke="#fff" stroke-width="2.5"/><path d="M24 18 L14 29 M17 26 L20 29" stroke="#fff" stroke-width="2.5"/></svg><span>Find your<br>keys</span></div>
  </div>
</section>

<!-- Page 3 -->
<section class="page page--three">
  <svg class="deco" viewBox="0 0 376 504" preserveAspectRatio="none" aria-hidden="true">
    <path d="M0 180 C100 150 220 220 376 160 V0 H0Z" fill="var(--blue)" opacity=".25"/>
    <path d="M0 420 C120 380 250 460 376 400 V504 H0Z" fill="var(--blue)" opacity=".3"/>
  </svg>
  <div class="boxed-title" style="left:115px;top:32px;width:131px;height:32px;padding-top:8px;font-size:13px">Product In use</div>
  <ul class="use-list">
    <li><svg viewBox="0 0 16 16"><rect x="5" y="1" width="7" height="13" rx="1.5" fill="none" stroke="#fff" stroke-width="1.5"/></svg><span><strong>To locate your phone:</strong> Double press the finder to activate the alarm</span></li>
    <li><svg viewBox="0 0 16 16"><circle cx="11" cy="5" r="3" fill="none" stroke="#fff" stroke-width="1.5"/><path d="M9 7 L3 14 M5 11 L7 13" stroke="#fff" stroke-width="1.5"/></svg><span><strong>To Find your keys:</strong> Navigate to the "Device" tab and press the "Call" button</span></li>
    <li><svg viewBox="0 0 16 16"><rect x="3" y="2" width="10" height="7" rx="1" fill="#fff"/><rect x="7" y="9" width="2" height="6" fill="#fff"/></svg><span><strong>Selfie Remote:</strong> Navigate to the " Camera" tab in the app and single press the finder to take a picture.</span></li>
    <li><svg viewBox="0 0 16 16"><rect x="6" y="1" width="4" height="9" rx="2" fill="#fff"/><path d="M4 8 A4 4 0 0 0 12 8 M8 12 V15" fill="none" stroke="#fff" stroke-width="1.3"/></svg><span><strong>Lost Record:</strong> Navigate to the "Location" tab and press the "Lost Record" button to find the last location the device was disconnected on the map.</span></li>
  </ul>
  <div class="photo" role="img" aria-label="Counter display box filled with packaged trackers, with a photo of a hand holding keys and a tag" style="left:224px;top:196px;width:148px;height:304px;background:linear-gradient(160deg,#2b2b2b 0 18%,#dfe3e8 18%,#b9c6d3 70%,#ffffff)"></div>
  <h2 class="abs headline" style="left:9px;top:230px;font-size:21px;color:var(--white)">GETTING STARTED</h2>
  <p class="abs" style="left:9px;top:264px;width:208px;font-size:9px;line-height:1.4;color:var(--white)">Download the free "orbolink" app<br>Turn on the device with a long press<br>Open the app and press the "+" icon then select the <strong>Orbo Tag</strong> device to pair</p>
  <div class="boxed-title" style="left:9px;top:336px;width:131px;height:32px;padding-top:8px;font-size:13px">Success story</div>
  <p class="abs small" style="left:9px;top:382px;width:206px;color:var(--white)">We believe in finding lost things. After countless hours of research, we have created something we think every person can use. We hope to eliminate the frustration and confusion felt by the loss of a phone, keys or any other important item. Our mission is to give you the power to find every anything and everything all the time.</p>
  <div class="abs url" style="left:9px;top:474px;color:var(--white)">www.orbotag-demo.com</div>
</section>

</body>
</html>
```